Asset tracing and investigation firm requires marketing brochure for services

We need a professional looking brochure with layout that supports the text that we have already drafted, is easy on the eye and can easily be navigated by clients either electronic/screen format or printed format. The wording is not finalised and all aspects need to be remain editable (including the logo and picture(s)) - preferably in Word or similarly accessible format.

```html
<!DOCTYPE html>
<html lang="en">
<head>
<meta charset="utf-8">
<title>OSINT Tiers – ARVEN</title>
<link rel="stylesheet" href="https://fonts.googleapis.com/css2?family=Fira+Sans+Condensed:ital,wght@0,700;1,400;1,700&family=Tinos:wght@700&display=swap">
<style>
  :root {
    --page-bg: #d5eefa;
    --corner-bg: #ffffff;
    --ink: #1b1b24;
    --brand-blue: #1a4fb0;
    --brand-gold: #d3a62b;
  }
  * { margin: 0; padding: 0; box-sizing: border-box; }
  html, body { width: 1200px; height: 848px; overflow: hidden; }
  body {
    position: relative;
    background: var(--page-bg);
    color: var(--ink);
    font-family: "Fira Sans Condensed", "Arial Narrow", sans-serif;
  }
  .corner-panel { position: absolute; left: 0; top: 0; width: 360px; height: 150px; }
  .brand {
    position: absolute; left: 54px; top: 52px;
    display: flex; align-items: center; gap: 12px;
  }
  .brand-mark { width: 34px; height: 34px; background: var(--brand-gold); }
  .brand-name {
    font-family: "Tinos", "Times New Roman", serif;
    font-weight: 700; font-size: 42px; letter-spacing: 1px;
    color: var(--brand-blue); line-height: 1;
  }
  .tiers {
    position: absolute; left: 118px; top: 148px; width: 962px;
  }
  .tiers-title {
    font-family: "Tinos", "Times New Roman", serif;
    font-weight: 700; font-size: 21px; letter-spacing: 0.3px;
    text-decoration: underline; text-decoration-thickness: 1.5px;
    text-underline-offset: 3px; margin-bottom: 2px;
  }
  .tier {
    font-style: italic; font-size: 15.6px; line-height: 30px;
    letter-spacing: -0.1px;
  }
  .tier + .tier { margin-top: 30px; }
  .initial { font-weight: 700; font-style: italic; font-size: 19px; }
</style>
</head>
<body>
  <svg class="corner-panel" viewBox="0 0 360 150" aria-hidden="true">
    <path d="M0 0 H350 C346 70 300 112 220 125 L0 148 Z" fill="var(--corner-bg)"/>
  </svg>

  <div class="brand">
    <span class="brand-mark"></span>
    <span class="brand-name">ARVEN</span>
  </div>

  <main class="tiers">
    <h1 class="tiers-title">OSINT TIERS</h1>

    <p class="tier"><span class="initial">T</span>ier <span class="initial">O</span>ne OSINT sources are essential public and proprietary datasets and may include: Voters Roll Records, Consensual Marketing Data Footprints, Current Active Credit File Footprints, Land Registry, Landline, Mobile &amp; Ex-Directory (hidden) Telephone Records, Corporate Records, Other Proprietary Database Sources, Social Media, County Court Judgment Databases, High Court Judgment Databases, Bankruptcy Searches, Proprietary Database Shareholder Searches, Historical and Concurrent Credit File Footprints, House Prices Information Database Checks, Property Company Reverse Land Registry Enquiries, Probate / Inheritance, Company Credit Files and Accounts Analysis, Genealogy Databases &amp; Family Searches, Interim Charging Orders / Property Charge Databases, InsuranceData Indicators, One-the-ground Enquiries, Historical HM Land Registry searches, Corporate Payment Data, Risk Scores, Government Databases, Data Leaks, National Post Forwarding Database, Vehicle Finance Enquiries, International Corporate Databases, Regional News, Business Publications.</p>

    <p class="tier"><span class="initial">T</span>ier <span class="initial">T</span>wo sources may sit behind paywalls, require more advanced data mining/analysis or represent more time intensive investigations such as: Deep Internet, GRO enquiries, Human Intelligence /Source Enquiries, Third Party Credit Agency Enquiries, Local Language News Sources, Vehicle Finance Enquiries, Specialist Paywalled Data Repositories, Archived Domain &amp; Website Registration, Archived/ Hidden Corporate Data, Archived Voters Roll Footprint Searches, Local Authority Planning Application, Specialist Employment Checks.</p>

    <p class="tier"><span class="initial">T</span>ier <span class="initial">T</span>hree sources, enacted by specialists in their respective fields, require individual expert manipulation, the use of technology or AI, and/or sit behind advanced paywalls. These include: Dark Web, Engagement of Advanced Machine Learning and Artificial Intelligence Algorithms, Physical Attendances, Pre-Text Enquiries, Bank Account Searches (subject to GDPR conditions being satisfied), International Database Searches, In-Person Registry Searches, Physical Asset Identification, Large Data Gathering and Analysis Software.</p>
  </main>
</body>
</html>
```